Business card and company stationary - Corvane Cleaning Ltd

1. Who are we and who are our customers?

o We are a relatively new cleaning company, established December 2008. We are a small company. We have 24 staff and we offer domestic and commercial cleaning services.
o We both (me and my wife) have been working for many years in the cleaning industry. We worked for some of the biggest and best cleaning companies in UK. We’ve been operatives, supervisors and managers.
o Inevitably after so many years of working for someone else, we decided to start our own business.
o Our domestic customers are middle class families and busy professionals. We’ve got some commercial customers, mainly offices.
o We are growing steadily.

2. What do we do? What are our services?

o Cleaning. We’ve got range of services - not to many but still can be daunting and confusing for some.
o Generally we’ve got domestic and commercial clients. The approach to the domestic cleaning customers is different to the commercial. In the way we want to say that it is cleaning that we do, but we acknowledge the environment and we appreciate the personal circumstances and requirements that are present. We do care, we listen and we try to work out the best possible way to complete our work.
o Mainly we get our work through referrals

3. What do we want with our stationery ?

o To place and maintain our message and reach out to people and organisations
o We want to advertise, communicate and sale.
o We are going to sell services.
o Increase membership, loyalty and support.

We are after business card design, headed letter and compliment slip.
We would like the headed letter to be created in formats suitable for :
- printing format
- also for use in our daily correspondence via e mail with clients and staff in a easy to edit and write format

The website we have is still under contraction and the domain is corvanecleaning.example

Target Market(s)

Families, individuals, businesses.

Industry/Entity Type

Cleaning Service

Contact Information for Business Card

FRONT :
Company Name - Corvane Cleaning Ltd
Company address - 41 Pelbury Rd, Pelbury, Essex, RM14 7QT
Name - Mrs. Teodora Vasilkova - Tedi
Title - Managing Director
Company phone - 020 8837 2591
E mail - tedi.vasilkova@corvanecleaning.example

BACK :

Company website - corvanecleaning.example
E mail - enquiries@corvanecleaning.example

Font styles to use
Serif

Requirements
Must have
• The above items and company logo...maybe at the back. But I'm free for any suggestions.

```html
<!DOCTYPE html>
<html lang="en">
<head>
<meta charset="utf-8">
<title>Corvane Cleaning Ltd — Letterhead</title>
<link rel="stylesheet" href="https://fonts.googleapis.com/css2?family=Arimo:wght@400;700&family=Open+Sans:wght@400;600&display=swap">
<style>
  :root {
    --backdrop: #1f2833;
    --paper: #ffffff;
    --ink: #111111;
    --accent: #2dbdf0;
    --signature-tone: #e4e4e4;
  }
  * { box-sizing: border-box; margin: 0; padding: 0; }
  html, body { width: 1000px; height: 1200px; overflow: hidden; }
  body { background: var(--backdrop); position: relative; font-family: "Arimo", Arial, sans-serif; color: var(--ink); }

  .letterhead { position: absolute; left: 157px; top: 116px; width: 686px; height: 968px; background: var(--paper); }

  .brand-mark { position: absolute; left: 49px; top: 44px; display: flex; align-items: center; gap: 10px; }
  .brand-mark__circle { width: 26px; height: 26px; border: 4px solid var(--ink); border-radius: 50%; }
  .brand-mark__name { font-size: 15px; font-weight: 700; color: var(--ink); }

  .edge-tab { position: absolute; right: 0; top: 149px; width: 38px; height: 16px; background: var(--accent); }

  .letter { position: absolute; left: 102px; width: 482px; font-size: 13px; line-height: 16.6px; }
  .letter__date { top: 277px; }
  .letter__recipient { top: 309px; }
  .letter__salutation { top: 392px; }
  .letter__body { top: 426px; text-align: justify; hyphens: auto; }
  .letter__body p { margin-bottom: 16px; }
  .letter__closing { top: 657px; }
  .letter__signature { position: absolute; left: 86px; top: 678px; width: 150px; height: 58px; background: linear-gradient(90deg, var(--signature-tone), #f4f4f4); border-radius: 4px; }
  .letter__signer { top: 739px; }

  .footer { position: absolute; left: 0; top: 884px; width: 100%; }
  .footer__wordmark { position: absolute; left: 48px; top: 0; font-weight: 700; color: var(--ink); }
  .footer__wordmark-main { display: block; font-size: 24px; letter-spacing: 1px; line-height: 26px; }
  .footer__wordmark-sub { display: block; font-size: 11px; letter-spacing: 2.4px; line-height: 14px; }
  .footer__divider { position: absolute; left: 224px; top: 1px; width: 14px; height: 37px; background: var(--accent); }
  .footer__contacts { position: absolute; left: 268px; top: 0; font-family: "Open Sans", Arial, sans-serif; font-size: 12px; }
  .contact-row { display: flex; align-items: center; height: 16px; margin-bottom: 8px; white-space: nowrap; }
  .contact-item { display: inline-flex; align-items: center; gap: 6px; margin-right: 11px; }
  .contact-item svg { width: 11px; height: 11px; fill: var(--ink); }
  .contact-legal { font-size: 8.5px; margin-left: 5px; }
</style>
</head>
<body>
  <main class="letterhead">
    <div class="brand-mark">
      <span class="brand-mark__circle"></span>
      <span class="brand-mark__name">Corvane Cleaning Ltd</span>
    </div>
    <div class="edge-tab"></div>

    <p class="letter letter__date">June 16, 2016</p>
    <address class="letter letter__recipient" style="font-style:normal">
      First Last Name<br>Street Address<br>City, State 00000
    </address>
    <p class="letter letter__salutation">Dear :</p>
    <div class="letter letter__body">
      <p>Lorem ipsum dolor sit amet, consectetur adipiscing elit. Aenean ut ipsum eget massa hendrerit vestibulum vel in velit. Donec pretium neque velit.</p>
      <p>Aliquam porta lectus nec mauris ornare venenatis. Vivamus non est turpis, et cursus sem. Mauris vehicula erat in diam auctor at bibendum nisl lacinia.</p>
      <p>Morbi imperdiet neque vehicula nunc convallis gravida. Vestibulum iaculis pretium placerat. Integer consequat, est sit amet facilisis eleifend, nibh nibh varius orci, eget dapibus arcu dui non purus. Pellentesque in magna mauris. Duis enim sapien, dictum vitae condimentum a, pulvinar vel lacus. Mauris et molestie nibh. Vestibulum vitae nulla at metus elementum porta sit amet interdum elit. Nulla sollicitudin neque eu nulla volutpat congue.</p>
    </div>
    <p class="letter letter__closing">Sincerely,</p>
    <div class="letter__signature" role="img" aria-label="Handwritten signature of the sender"></div>
    <p class="letter letter__signer">Admin</p>

    <footer class="footer">
      <div class="footer__wordmark">
        <span class="footer__wordmark-main">CORVANE</span>
        <span class="footer__wordmark-sub">CLEANING LTD</span>
      </div>
      <div class="footer__divider"></div>
      <div class="footer__contacts">
        <div class="contact-row">
          <span class="contact-item">
            <svg viewBox="0 0 24 24" aria-hidden="true"><path d="M6.6 10.8a15.1 15.1 0 0 0 6.6 6.6l2.2-2.2a1 1 0 0 1 1-.25 11.4 11.4 0 0 0 3.6.57 1 1 0 0 1 1 1V20a1 1 0 0 1-1 1A17 17 0 0 1 3 4a1 1 0 0 1 1-1h3.5a1 1 0 0 1 1 1c0 1.25.2 2.45.57 3.57a1 1 0 0 1-.25 1z"/></svg>
            088 8888 888
          </span>
          <span class="contact-item" style="gap:2px">
            <svg viewBox="0 0 24 24" aria-hidden="true"><path d="M12 2a10 10 0 1 0 5 18.7l-1-1.7A8 8 0 1 1 20 12v1.2a1.8 1.8 0 0 1-3.6 0V12a4.4 4.4 0 1 0-1.3 3.1A3.8 3.8 0 0 0 22 13.2V12A10 10 0 0 0 12 2zm0 12.4a2.4 2.4 0 1 1 0-4.8 2.4 2.4 0 0 1 0 4.8z"/></svg>
            name@email.com
          </span>
          <span class="contact-item" style="gap:3px">
            <svg viewBox="0 0 24 24" aria-hidden="true"><path d="M12 2a10 10 0 1 0 0 20 10 10 0 0 0 0-20zm6.9 6h-2.9a15.6 15.6 0 0 0-1.4-3.6A8 8 0 0 1 18.9 8zM12 4c.8 1.2 1.5 2.5 1.9 4h-3.8c.4-1.5 1.1-2.8 1.9-4zM4.3 14a8 8 0 0 1 0-4h3.4a16.5 16.5 0 0 0 0 4zm.8 2h2.9c.3 1.3.8 2.5 1.4 3.6A8 8 0 0 1 5.1 16zM8 8H5.1a8 8 0 0 1 4.3-3.6C8.8 5.5 8.3 6.7 8 8zm4 12c-.8-1.2-1.5-2.5-1.9-4h3.8c-.4 1.5-1.1 2.8-1.9 4zm2.3-6H9.7a14.7 14.7 0 0 1 0-4h4.6a14.7 14.7 0 0 1 0 4zm.3 5.6c.6-1.1 1.1-2.3 1.4-3.6h2.9a8 8 0 0 1-4.3 3.6zm1.7-5.6a16.5 16.5 0 0 0 0-4h3.4a8 8 0 0 1 0 4z"/></svg>
            www.corvanecleaning.example
          </span>
        </div>
        <div class="contact-row">
          <span class="contact-item" style="gap:8px">
            <svg viewBox="0 0 24 24" aria-hidden="true"><path d="M12 3 2 12h3v8h5v-6h4v6h5v-8h3z"/></svg>
            Address, Adress. 00000
          </span>
          <span class="contact-legal">Company No: 00000&nbsp; | &nbsp;VAT : 000000000</span>
        </div>
      </div>
    </footer>
  </main>
</body>
</html>
```